Life Coaching business needs a new flyer

We are an Australian business that specialises in Life Coaching, Career Coaching, Health and Wellness Coaching, Yoga and Pilates. We need a A4 double sided flyer that is full colour and folded to DL format. I have attached a couple of designs that I like and some pictures and would like the flyer to be bright yet stylish.

Life Coaching

```html
<!DOCTYPE html>
<html lang="en">
<head>
<meta charset="utf-8">
<title>Clearpath Coaching – DL Flyer</title>
<link rel="stylesheet" href="https://fonts.googleapis.com/css2?family=Crimson+Text:wght@400;600;700&family=PT+Sans:ital,wght@0,400;0,700;1,400&family=Great+Vibes&display=swap">
<style>
:root{
  --bg:#b3b3b3;
  --blue:#0aa3e6;
  --blue-deep:#0a86c9;
  --blue-head:#1b8fc9;
  --sky:#cfeaf7;
  --green:#4cae1e;
  --green-dark:#3a9612;
  --ink:#3b3b3b;
  --white:#ffffff;
}
*{margin:0;padding:0;box-sizing:border-box}
html,body{width:874px;height:1200px;overflow:hidden;background:var(--bg)}
body{position:relative;font-family:"PT Sans",sans-serif;color:var(--ink)}
.sheet{position:absolute;left:69px;width:705px;height:499px;background:var(--white);overflow:hidden;box-shadow:0 2px 6px rgba(0,0,0,.25)}
.sheet--outside{top:75px}
.sheet--inside{top:626px}
.panel{position:absolute;top:0;height:499px}
.abs{position:absolute}
.photo{position:absolute}
.heading{font-family:"Crimson Text",serif;font-weight:600;color:var(--blue-head);line-height:1.05}
.body-copy{font-size:7.6px;line-height:9.6px;text-align:justify}
.body-copy p{margin-bottom:7px}
.brand{font-family:"Crimson Text",serif;font-weight:600;letter-spacing:.5px;display:flex;align-items:center;gap:6px}
.brand-dot{width:12px;height:12px;border-radius:50%;flex:none}
/* outside */
.testimonials{left:0;width:234px}
.testimonials .heading{position:absolute;left:26px;top:22px;font-size:14px}
.testimonials .body-copy{position:absolute;left:26px;top:47px;width:178px;font-size:6.9px;line-height:9.5px}
.contact{left:234px;width:236px;background:var(--blue);height:274px}
.contact .intro{position:absolute;left:27px;top:24px;width:182px;font-size:7px;line-height:9.6px;color:var(--white)}
.contact .intro p{margin-bottom:6px}
.contact .brand{position:absolute;left:0;width:236px;top:140px;justify-content:center;color:var(--white);font-size:13px}
.contact-title{position:absolute;top:194px;width:236px;text-align:center;font-family:"Crimson Text",serif;font-weight:700;color:var(--white);font-size:16px}
.contact-lines{position:absolute;top:216px;width:236px;text-align:center;font-family:"Crimson Text",serif;font-weight:700;color:var(--white);font-size:10.4px;line-height:14px}
.offer{position:absolute;left:234px;top:440px;width:236px;height:59px;background:var(--green);color:var(--white);font-family:"Crimson Text",serif;font-weight:600;font-size:10.6px;line-height:14.4px;text-align:center;padding-top:6px}
.cover{left:470px;width:235px}
.cover .brand{position:absolute;left:0;width:235px;top:108px;justify-content:center;color:var(--blue-deep);font-size:13.5px}
.services{position:absolute;left:470px;top:370px;width:220px;font-family:"Great Vibes",cursive;color:var(--white);font-size:27px;line-height:36px;text-align:right}
.services li{list-style:none;display:flex;justify-content:flex-end;align-items:center;gap:10px}
.services li span.icon{width:18px;height:18px;border:1.5px solid var(--white);border-radius:50%;display:inline-block}
/* inside */
.intro-panel{left:0;width:234px}
.questions{position:absolute;left:26px;top:23px;width:180px;font-size:7.8px;line-height:10.8px;font-weight:700;color:#222}
.questions p{margin-bottom:6px}
.intro-panel .heading{position:absolute;left:26px;top:164px;font-size:13.5px;width:190px}
.intro-panel .body-copy{position:absolute;left:26px;top:202px;width:178px;font-size:7.8px;line-height:11.4px;text-align:left}
.intro-panel .body-copy p{margin-bottom:9px}
.coaching-panel{left:234px;width:236px}
.coaching-panel .heading{font-size:13.5px;margin-bottom:2px}
.coaching-panel .block{position:absolute;left:26px;width:180px}
.coaching-panel .body-copy{font-size:7.9px;line-height:11.4px}
.coaching-panel .brand{position:absolute;left:30px;top:325px;color:var(--blue-deep);font-size:11.5px}
.help-panel{left:470px;width:235px}
.help-panel .block{position:absolute;left:26px;width:180px}
.help-panel .heading{font-size:13.5px;margin-bottom:2px}
.help-panel .body-copy{font-size:7.9px;line-height:11.4px}
.help-list{list-style:none;font-size:7.8px;line-height:11.4px;font-style:italic;margin-top:5px}
.help-list li{display:flex;gap:6px;align-items:flex-start}
.help-list svg{flex:none;margin-top:2px}
.overlay{position:absolute;right:30px;width:180px;text-align:right;color:var(--white)}
.overlay .heading{color:var(--white);font-size:13.5px}
.overlay p{font-size:7.9px;line-height:11.4px}
</style>
</head>
<body>

<!-- OUTSIDE -->
<section class="sheet sheet--outside">
  <div class="panel testimonials">
    <h2 class="heading">Happy Clients Testimonials</h2>
    <div class="body-copy">
      <p>“I have lost 10 kilos and now have the energy to play with my kids. Thanks Mara for you support/guidance and helping me get rid of my limiting beliefs. I feel I can achieve anything now! The sky’s the limit” Tessa, Mosman</p>
      <p>“I had always wanted to start up own café however every time it came to putting it into practice I would procrastinate and not achieve anything. I became overwhelmed with the whole process and never achieved anything. Mara put it into bite sized chunks and helped me to set small achievable goals. I am now a happy café owner.” Priya, Double Bay</p>
      <p>“Mara has helped to change my life around in all aspects. I would have been lost without her. Thanks Mara for your professionalism, support and guidance.” Elena, Cremorne</p>
      <p>“I was so busy with kids, work, and my husband I lost who I was. Mara has helped me find the person I am again.” Joanne, Chatswood</p>
      <p>“When I started with Coach Mara, I didn’t know anything about coaching. I called her because she helped a friend of mine make a career change that was a perfect fit for her. I had the opportunity to make a change too and did not know where to start. I am now in a job that I love. I would recommend Mara to everyone.” Daniel, Texas America</p>
    </div>
    <svg class="abs" style="left:0;top:360px" width="234" height="40" viewBox="0 0 234 40">
      <path d="M0,0 C80,6 160,8 234,12 L234,26 C160,22 80,20 0,20 Z" fill="var(--green)"/>
    </svg>
    <div class="photo" style="left:0;top:386px;width:234px;height:113px;background:linear-gradient(180deg,#5ea9dc,#a9d3ef)" role="img" aria-label="Photo of four friends jumping joyfully against a blue sky"></div>
    <svg class="abs" style="left:0;top:360px" width="234" height="40" viewBox="0 0 234 40">
      <path d="M0,0 C80,6 160,8 234,12 L234,26 C160,22 80,20 0,20 Z" fill="var(--green)"/>
    </svg>
  </div>

  <div class="panel contact">
    <div class="intro">
      <p>Clearpath Coaching and Meditation Studio is a professional service that can help you achieve the goals that you are looking for in Life Coaching, Meditation, and Yoga/Pilates.</p>
      <p>If you are ready to take your life to the next level and would like to know more, please</p>
    </div>
    <div class="brand"><span class="brand-dot" style="border:1.5px solid var(--white)"></span>CLEARPATH COACHING</div>
    <div class="contact-title">contact us.</div>
    <div class="contact-lines">
      Phone : 02 9000 4127<br>
      hello@clearpathcoaching.com.au<br>
      www.clearpathcoaching.com.au
    </div>
  </div>
  <div class="photo" style="left:234px;top:274px;width:236px;height:166px;background:linear-gradient(180deg,#6b6b6b,#2f2f2f)" role="img" aria-label="Portrait photo of the two coaches, a woman and a man, smiling"></div>
  <div class="offer">Free Introductory Life Coaching<br>Phone/Skype session - 20 mins<br>(To see if coaching is right for you)</div>

  <div class="panel cover">
    <svg class="abs" style="left:0;top:0" width="235" height="499" viewBox="0 0 235 499">
      <defs>
        <linearGradient id="coverBlue" x1="0" y1="0" x2="0" y2="1">
          <stop offset="0" stop-color="#23b0ee"/><stop offset="1" stop-color="#0a8fd3"/>
        </linearGradient>
      </defs>
      <rect width="235" height="499" fill="url(#coverBlue)"/>
      <path d="M0,0 H235 V170 C200,160 0,150 0,150 Z" fill="var(--sky)"/>
    </svg>
    <div class="photo" style="left:0;top:150px;width:235px;height:220px;background:linear-gradient(180deg,#dfe7ec,#b9ccd8);clip-path:path('M0,0 L235,20 L235,30 C190,120 110,160 0,190 Z')" role="img" aria-label="Photo of a man and woman in yoga tree pose on a beach"></div>
    <svg class="abs" style="left:0;top:150px" width="235" height="220" viewBox="0 0 235 220">
      <path d="M235,40 C190,125 110,168 0,195 L0,202 C115,176 195,135 235,60 Z" fill="var(--green)"/>
      <path d="M235,30 C190,120 110,160 0,190 L0,195 C110,168 190,125 235,40 Z" fill="var(--white)"/>
    </svg>
    <div class="brand"><span class="brand-dot" style="background:var(--green)"></span>CLEARPATH COACHING</div>
  </div>
  <ul class="services">
    <li>Life Coaching <span class="icon"></span></li>
    <li>Meditation <span class="icon"></span></li>
    <li>Yoga/Pilates <span class="icon"></span></li>
  </ul>
</section>

<!-- INSIDE -->
<section class="sheet sheet--inside">
  <div class="photo" style="left:0;top:380px;width:234px;height:119px;background:linear-gradient(180deg,#6fb8e6,#d7edf8)" role="img" aria-label="Photo of a woman in a balancing yoga pose by the sea"></div>
  <div class="photo" style="left:234px;top:360px;width:236px;height:139px;background:linear-gradient(135deg,#8a5a2e,#e2b58d)" role="img" aria-label="Photo of a smiling mother hugging her young daughter"></div>
  <div class="photo" style="left:470px;top:150px;width:235px;height:349px;background:linear-gradient(180deg,#bfe3f5,#2aa6e2 45%,#1590d2)" role="img" aria-label="Photo of a smiling man, tinted blue"></div>
  <svg class="abs" style="left:0;top:0" width="705" height="499" viewBox="0 0 705 499">
    <path d="M0,0 H705 V165 C620,300 420,350 0,366 Z" fill="var(--white)"/>
    <path d="M705,165 C620,300 420,350 0,366 L0,390 C420,378 630,320 705,178 Z" fill="var(--green)"/>
    <path d="M705,178 C630,320 420,378 0,390 L0,394 C420,382 632,324 705,184 Z" fill="var(--white)"/>
  </svg>

  <div class="panel intro-panel">
    <div class="questions">
      <p>Are you looking at making changes this year?</p>
      <p>Are you stuck in a rut or at a crossroad in your life?</p>
      <p>Are you wanting to lose weigh but can’t get motivated?</p>
      <p>Do you have ongoing problems with your career, relationships, or just life itself?</p>
      <p>Life coaching is the answer</p>
    </div>
    <h2 class="heading">Clearpath Coaching and Meditation Studio</h2>
    <div class="body-copy">
      <p>Our mission is to help you become the best possible person you can be. Mentally, physically, and spiritually.</p>
      <p>We offer highly qualified and compassionate trainers/coaches for Life Coaching, Meditation, Yoga and Pilates.</p>
      <p>They will guide and motivate you every step of the way to achieve all your dreams and goals.</p>
      <p>They will make you be the best you can be</p>
    </div>
  </div>

  <div class="panel coaching-panel">
    <div class="block" style="top:18px">
      <h2 class="heading">Life Coaching</h2>
      <div class="body-copy">
        <p>Your Life Coach will give you the confidence and the ability to move forward in a positive manner in all areas of your life where you crave change.</p>
        <p>Life Coaching is about breaking down the barriers preventing this change from happening, and creating the ideal environment for positive action to take place. It is a holistic approach, which looks at the present and sets goals for a totally successful future.</p>
      </div>
    </div>
    <div class="block" style="top:173px">
      <h2 class="heading">Career Coaching</h2>
      <div class="body-copy">
        <p>Are you at a crossroads in your career and at a loss about what to do next? Do you want your work to be in alignment with the authentic you? It can be difficult to assess career options, goals, and strategies, and have the confidence to implement changes on your own. With the right coaching support, you will gain the clarity that you need to take control and have a fulfilling and rewarding career.</p>
      </div>
    </div>
    <div class="brand"><span class="brand-dot" style="background:var(--green)"></span>CLEARPATH COACHING</div>
  </div>

  <div class="panel help-panel">
    <div class="block" style="top:19px">
      <h2 class="heading">Wellness Coaching</h2>
      <div class="body-copy">
        <p>Health and wellness coaches help their clients find the motivation and tools to achieve their health and wellness goals, working with the client to examine and improve the psychological framework that supports those goals.</p>
      </div>
    </div>
    <div class="block" style="top:111px">
      <h2 class="heading">Why Would I Need Help?</h2>
      <div class="body-copy" style="text-align:left">
        Coaching is for anyone who wants to make lasting changes in their life.<br>Coaching can assist with such issues as:
      </div>
      <ul class="help-list">
        <li><svg width="10" height="8" viewBox="0 0 10 8"><path d="M1,4 L4,7 L9,1" fill="none" stroke="var(--green)" stroke-width="1.8"/></svg>Creating a better work- life balance</li>
        <li><svg width="10" height="8" viewBox="0 0 10 8"><path d="M1,4 L4,7 L9,1" fill="none" stroke="var(--green)" stroke-width="1.8"/></svg>Resolving relationship issues</li>
        <li><svg width="10" height="8" viewBox="0 0 10 8"><path d="M1,4 L4,7 L9,1" fill="none" stroke="var(--green)" stroke-width="1.8"/></svg>Career guidance</li>
        <li><svg width="10" height="8" viewBox="0 0 10 8"><path d="M1,4 L4,7 L9,1" fill="none" stroke="var(--green)" stroke-width="1.8"/></svg>Stress management</li>
        <li><svg width="10" height="8" viewBox="0 0 10 8"><path d="M1,4 L4,7 L9,1" fill="none" stroke="var(--green)" stroke-width="1.8"/></svg>Weight loss and fitness</li>
        <li><svg width="10" height="8" viewBox="0 0 10 8"><path d="M1,4 L4,7 L9,1" fill="none" stroke="var(--green)" stroke-width="1.8"/></svg>Motivation and goal setting</li>
        <li><svg width="10" height="8" viewBox="0 0 10 8"><path d="M1,4 L4,7 L9,1" fill="none" stroke="var(--green)" stroke-width="1.8"/></svg>Boosting your self esteem</li>
        <li><svg width="10" height="8" viewBox="0 0 10 8"><path d="M1,4 L4,7 L9,1" fill="none" stroke="var(--green)" stroke-width="1.8"/></svg>Overcoming negative emotions &amp; thoughts</li>
        <li><svg width="10" height="8" viewBox="0 0 10 8"><path d="M1,4 L4,7 L9,1" fill="none" stroke="var(--green)" stroke-width="1.8"/></svg>Better time management</li>
      </ul>
    </div>
    <div class="overlay" style="top:348px">
      <h2 class="heading">Meditation</h2>
      <p>We specialise in teaching meditation from beginners to advanced and teach a variety of techniques for stress reduction, peace of mind, stillness, and clarity.</p>
    </div>
    <div class="overlay" style="top:416px">
      <h2 class="heading">Yoga/Pilates</h2>
      <p>Your highly qualified and experienced Yoga or Pilates instructor will come to you and create a fun and varied workout based on what you enjoy and what your goals are.</p>
    </div>
  </div>
</section>

</body>
</html>
```